Freelance Translator in Need of a Business Card

I am a freelance Japanese to English translator. I work in the video game localization industry and do literary translation in my spare time. I would like to have both the English word 'Translator' and the Japanese '翻訳者' in the job title. The final design should evoke trust, openness, and reliability.

Target Market(s)

Video game localization companies
Japanese comic book artists

Industry/Entity Type

Business

Contact Information for Business Card

Daniel Oskerby, Translator
dan.oskerby@fernlowmail.com
velmotranslates.com
twitter: @velmo_tl

Colors

Designer to choose colors to be used in the design.

```html
<!DOCTYPE html>
<html lang="en">
<head>
<meta charset="utf-8">
<title>Daniel Oskerby – Translator Business Card</title>
<link rel="stylesheet" href="https://fonts.googleapis.com/css2?family=Open+Sans:wght@400;600;700&family=Noto+Sans+JP:wght@400&display=swap">
<style>
  :root {
    --backdrop: #e9ebec;
    --card: #f7f8f8;
    --card-edge: #9fa3a5;
    --brand-blue: #1f4f7d;
    --ink: #2f3336;
  }
  html, body {
    margin: 0;
    padding: 0;
    width: 1200px;
    height: 970px;
    overflow: hidden;
    background: var(--backdrop);
  }
  .business-card {
    position: absolute;
    left: 170px;
    top: 246px;
    width: 860px;
    height: 478px;
    background: var(--card);
    border: 1px solid var(--card-edge);
    border-radius: 24px;
    box-sizing: border-box;
    font-family: "Open Sans", sans-serif;
    color: var(--ink);
  }
  .brand-name {
    position: absolute;
    left: 96px;
    top: 148px;
    width: 270px;
    height: 180px;
    display: flex;
    align-items: center;
    justify-content: center;
    gap: 12px;
    font-family: "Open Sans", sans-serif;
    font-weight: 600;
    font-size: 28px;
    color: var(--brand-blue);
    white-space: nowrap;
  }
  .brand-dot {
    width: 14px;
    height: 14px;
    border-radius: 50%;
    background: var(--brand-blue);
    flex: none;
  }
  .divider {
    position: absolute;
    left: 428px;
    top: 148px;
    width: 3px;
    height: 184px;
    background: var(--brand-blue);
  }
  .identity {
    position: absolute;
    left: 483px;
    top: 142px;
  }
  .person-name {
    margin: 0;
    font-weight: 700;
    font-size: 25px;
    line-height: 32px;
    letter-spacing: 0.3px;
    color: var(--brand-blue);
    text-transform: uppercase;
  }
  .job-title {
    margin: 0;
    font-size: 19px;
    line-height: 26px;
    color: var(--ink);
  }
  .job-title .ja {
    font-family: "Noto Sans JP", sans-serif;
  }
  .contact-list {
    position: absolute;
    left: 483px;
    top: 242px;
    margin: 0;
    padding: 0;
    list-style: none;
    font-size: 19px;
    color: var(--ink);
  }
  .contact-list li {
    display: flex;
    align-items: center;
    gap: 9px;
    height: 28px;
  }
  .contact-list li.social { margin-bottom: 10px; }
  .contact-icon {
    width: 17px;
    height: 17px;
    flex: none;
  }
  .social-dot {
    width: 15px;
    height: 15px;
    margin: 0 1px;
    border-radius: 50%;
    background: var(--brand-blue);
    flex: none;
  }
</style>
</head>
<body>
  <section class="business-card" aria-label="Business card of Daniel Oskerby, translator">
    <div class="brand-name"><span class="brand-dot"></span>Velmo Translates</div>
    <div class="divider"></div>
    <div class="identity">
      <h1 class="person-name">Daniel Oskerby</h1>
      <p class="job-title">Translator / <span class="ja" lang="ja">翻訳者</span></p>
    </div>
    <ul class="contact-list">
      <li class="social"><span class="social-dot"></span>@velmo_tl</li>
      <li>
        <svg class="contact-icon" viewBox="0 0 17 17" aria-hidden="true">
          <rect x="1" y="4" width="15" height="10" fill="var(--brand-blue)"/>
          <path d="M1.5 4.5 L8.5 10 L15.5 4.5" fill="none" stroke="#fff" stroke-width="1.3"/>
        </svg>
        dan.oskerby@fernlowmail.com
      </li>
      <li>
        <svg class="contact-icon" viewBox="0 0 17 17" aria-hidden="true">
          <circle cx="8" cy="8" r="6.5" fill="none" stroke="var(--brand-blue)" stroke-width="2"/>
          <path d="M1.5 8 H14.5 M8 1.5 C5 5 5 11 8 14.5 M8 1.5 C11 5 11 11 8 14.5" fill="none" stroke="var(--brand-blue)" stroke-width="1.2"/>
          <path d="M9 9 L16 12 L13 13 L12 16 Z" fill="var(--brand-blue)" stroke="#fff" stroke-width="0.8"/>
        </svg>
        velmotranslates.com
      </li>
    </ul>
  </section>
</body>
</html>
```